Creative Stationary for Solo Law Firm

I am looking for stationary designs for my solo law firm called TM Halvorsen Law PLLC. My logo is attached. I'd like the logo incorporated into the design.

I'm looking for a stationary design that is a bit outside of the box and not too standard or boring. The final design should communicate professionalism.

Target Market(s)

United States Clients, Opposing Counsel

Industry/Entity Type

Legal

Font styles to use
Sans Serif

Requirements
Must have
• The stationary design must incorporate my logo design attached. The design itself must be creative. The envelope design must follow standard United States designs with room for the postage stamp at the top right corner and space for the recipient's address in the middle.

```html
<!DOCTYPE html>
<html lang="en">
<head>
<meta charset="utf-8">
<title>TM Halvorsen Law — Stationery</title>
<link rel="stylesheet" href="https://fonts.googleapis.com/css2?family=Cinzel:wght@500&family=Arimo:wght@400;700&display=swap">
<style>
  :root {
    --navy: #18346b;
    --grey: #a8a8a8;
    --grey-light: #d9d9d9;
    --paper: #f3f3f3;
    --backdrop: #ebebeb;
    --ink: #4a4a4a;
    --white: #ffffff;
  }
  * { box-sizing: border-box; margin: 0; padding: 0; }
  html, body { width: 1200px; height: 925px; overflow: hidden; }
  body { background: var(--backdrop); position: relative; font-family: "Arimo", sans-serif; color: var(--ink); }

  .piece { position: absolute; background: var(--paper); overflow: hidden; box-shadow: 0 1px 3px rgba(0,0,0,.12); }
  .piece > svg.shapes { position: absolute; inset: 0; width: 100%; height: 100%; }
  .brand-name { font-family: "Cinzel", serif; font-weight: 500; color: var(--navy); white-space: nowrap; position: absolute; letter-spacing: .01em; }

  /* Letterhead */
  .letterhead { left: 230px; top: 116px; width: 340px; height: 482px; }
  .letterhead .brand-name { top: 24px; left: 0; right: 0; text-align: center; font-size: 14px; }
  .letterhead .footer { position: absolute; left: 0; right: 0; top: 445px; text-align: center; font-size: 5.6px; line-height: 9px; }
  .letterhead .footer b { color: var(--navy); }

  /* Presentation folder */
  .folder { left: 630px; top: 94px; width: 402px; height: 506px; background: var(--navy); }
  .folder .brand-name { top: 232px; left: 0; right: 0; text-align: center; font-size: 32px; color: var(--white); }

  /* Business cards */
  .card-front { left: 107px; top: 640px; width: 154px; height: 88px; }
  .card-front .brand-name { top: 21px; left: 0; right: 0; text-align: center; font-size: 9.5px; }
  .card-front .holder { position: absolute; top: 46px; right: 80px; text-align: right; font-size: 3.8px; line-height: 5.5px; }
  .card-front .holder strong { color: var(--navy); font-size: 5px; }
  .card-front .divider { position: absolute; top: 47px; left: 78px; width: .5px; height: 24px; background: var(--grey); }
  .card-front .contacts { position: absolute; top: 46px; left: 82px; font-size: 3.8px; line-height: 5.5px; }
  .card-front .contacts i { display: inline-block; width: 3px; height: 3px; background: var(--navy); margin-right: 2px; vertical-align: middle; }

  .card-back { left: 107px; top: 752px; width: 154px; height: 88px; background: var(--grey); }
  .card-back .brand-name { top: 37px; left: 0; right: 0; text-align: center; font-size: 11px; }
  .card-back .web { position: absolute; bottom: 8px; left: 0; right: 0; text-align: center; font-size: 3.8px; letter-spacing: .15em; color: var(--white); }

  /* Compliment slip */
  .slip { left: 301px; top: 653px; width: 381px; height: 183px; }
  .slip .brand-name { top: 28px; left: 17px; font-size: 11.5px; }
  .slip .address { position: absolute; left: 17px; top: 155px; font-size: 5.6px; line-height: 8px; }

  /* Envelope */
  .envelope { left: 720px; top: 653px; width: 381px; height: 183px; }
  .envelope .brand-name { top: 27px; left: 0; right: 0; text-align: center; font-size: 12.5px; color: var(--white); }
</style>
</head>
<body>

<section class="piece letterhead" aria-label="Letterhead">
  <svg class="shapes" viewBox="0 0 340 482" preserveAspectRatio="none">
    <path d="M0 0 H340 V3 Q150 6 0 34 Z" fill="var(--grey)"/>
    <path d="M40 482 Q230 478 340 452 V482 Z" fill="var(--navy)"/>
  </svg>
  <div class="brand-name">TM Halvorsen Law</div>
  <div class="footer">
    2170 Alder Crest Road, Brookhaven, NY 11719<br>
    <b>P :</b> 555 0142 7788 &nbsp;<b>C :</b> 555 0199 3021 &nbsp;<b>E :</b> marcus@halvorsenlaw.com &nbsp;<b>W :</b> www.halvorsenlaw.com
  </div>
</section>

<section class="piece folder" aria-label="Presentation folder">
  <svg class="shapes" viewBox="0 0 402 506" preserveAspectRatio="none">
    <path d="M0 0 H402 V2 Q140 6 0 36 Z" fill="var(--grey)"/>
    <path d="M0 506 Q260 500 402 476 V506 Z" fill="var(--grey-light)"/>
  </svg>
  <div class="brand-name">TM Halvorsen Law</div>
</section>

<section class="piece card-front" aria-label="Business card front">
  <svg class="shapes" viewBox="0 0 154 88" preserveAspectRatio="none">
    <path d="M0 0 H154 V2 Q60 6 0 18 Z" fill="var(--grey)"/>
    <path d="M40 88 Q120 86 154 76 V88 Z" fill="var(--navy)"/>
  </svg>
  <div class="brand-name">TM Halvorsen Law</div>
  <div class="holder"><strong>MARCUS LINDELL</strong><br>President<br>2170 Alder Crest Road<br>Brookhaven, NY 11719</div>
  <div class="divider"></div>
  <div class="contacts"><i></i>555 0142 7788<br><i></i>555 0199 3021<br><i></i>marcus@halvorsenlaw.com<br><i></i>www.halvorsenlaw.com</div>
</section>

<section class="piece card-back" aria-label="Business card back">
  <div class="brand-name">TM Halvorsen Law</div>
  <div class="web">www.halvorsenlaw.com</div>
</section>

<section class="piece slip" aria-label="Compliment slip">
  <svg class="shapes" viewBox="0 0 381 183" preserveAspectRatio="none">
    <path d="M0 0 H381 V1 Q130 4 0 28 Z" fill="var(--grey)"/>
    <path d="M90 183 Q300 180 381 152 V183 Z" fill="var(--navy)"/>
  </svg>
  <div class="brand-name">TM Halvorsen Law</div>
  <div class="address">2170 Alder Crest Road<br>Brookhaven, NY 11719</div>
</section>

<section class="piece envelope" aria-label="Envelope">
  <svg class="shapes" viewBox="0 0 381 183" preserveAspectRatio="none">
    <path d="M0 0 H381 L374 54 Q373 63 364 63 H17 Q8 63 7 54 Z" fill="var(--navy)"/>
  </svg>
  <div class="brand-name">TM Halvorsen Law</div>
</section>

</body>
</html>
```